CASH PAYMENT DISCOUNT NOTICE POSTED IN CASH REGISTER AREA

LOOKING TO MAKE A FLYER OR A POSTED NOTICE FOR CUSTOMERS PAYING FOR OVER-THE-COUNTER MERCHANDISE AND WHO PAY BY CASH METHOD TO GET A 4% CASH DISCOUNT.
PRESCRIPTIONS ARE EXCLUDED FROM THIS CASH DISCOUNT.

Target Market(s)

RETAIL CUSTOMERS

Industry/Entity Type

RETAIL PHARMACY

Colors
0054AA
0677BA
7BADD7
CADEEF
E8F1F8
EB3D1F
EC4F4E
F09395
F8D3D4
FCEDEE

Requirements
Must have
• LOGO COLORS
Nice to have
• EYE CATCHING

```html
<!DOCTYPE html>
<html lang="en">
<head>
<meta charset="utf-8">
<title>Cash Discount Notice</title>
<link rel="stylesheet" href="https://fonts.googleapis.com/css2?family=Montserrat:wght@800;900&family=Bebas+Neue&display=swap">
<style>
  :root {
    --blue: #0054aa;
    --blue-deep: #0677ba;
    --red: #eb3d1f;
    --red-soft: #ec4f4e;
    --pink: #f09395;
    --blush: #f8d3d4;
    --yellow: #fff200;
    --yellow-shade: #ffc51a;
    --white: #ffffff;
    --page: #e2e1e2;
  }
  html, body {
    margin: 0;
    padding: 0;
    width: 1200px;
    height: 2374px;
    overflow: hidden;
    background: var(--page);
  }
  .notice {
    position: absolute;
    left: 50px;
    top: 408px;
    width: 1100px;
    height: 1557px;
    display: block;
  }
  .headline { font-family: "Montserrat", sans-serif; font-weight: 800; }
  .condensed { font-family: "Bebas Neue", sans-serif; font-weight: 400; }
  .heavy { font-family: "Montserrat", sans-serif; font-weight: 900; }
  .footer-note { font-family: "Montserrat", sans-serif; font-weight: 800; }
</style>
</head>
<body>
<svg class="notice" viewBox="0 0 908 1285" xmlns="http://www.w3.org/2000/svg">
  <defs>
    <linearGradient id="field-glow" x1="0" y1="1" x2="1" y2="0">
      <stop offset="0" stop-color="#a04aa0"/>
      <stop offset="0.4" stop-color="#e0449b"/>
      <stop offset="0.7" stop-color="#ec4f4e" stop-opacity="0.85"/>
      <stop offset="1" stop-color="#f7941d"/>
    </linearGradient>
    <linearGradient id="burst-glow" x1="0" y1="0" x2="0" y2="1">
      <stop offset="0" stop-color="#f8d3d4"/>
      <stop offset="1" stop-color="#ffffff"/>
    </linearGradient>
  </defs>

  <!-- colour field -->
  <rect class="field" x="0" y="0" width="908" height="1285" fill="url(#field-glow)"/>

  <!-- top band -->
  <rect class="band-top-edge" x="0" y="170" width="908" height="10" fill="var(--white)"/>
  <rect class="band-top" x="0" y="0" width="908" height="170" fill="var(--blue)"/>
  <g class="title-dots" fill="var(--white)">
    <circle cx="60" cy="91" r="9"/><circle cx="80" cy="91" r="5"/><circle cx="95" cy="91" r="4"/><circle cx="109" cy="91" r="3"/>
    <circle cx="799" cy="91" r="3"/><circle cx="813" cy="91" r="4"/><circle cx="828" cy="91" r="5"/><circle cx="848" cy="91" r="9"/>
  </g>
  <text class="headline" x="454" y="124" font-size="96" fill="var(--yellow)" text-anchor="middle">Special Offer</text>

  <!-- bottom band -->
  <rect class="band-bottom-edge" x="0" y="1120" width="908" height="12" fill="var(--yellow)"/>
  <rect class="band-bottom" x="0" y="1132" width="908" height="153" fill="var(--blue)"/>

  <!-- burst artwork area -->
  <rect class="burst-art" x="150" y="265" width="600" height="290" rx="18" fill="url(#burst-glow)"
        role="img" aria-label="Starburst with two megaphones and radiating rays"/>

  <!-- yellow panel -->
  <polygon class="panel-shade" fill="var(--yellow-shade)" points="700,548 820,548 825,580 770,910 690,915"/>
  <polygon class="panel" fill="var(--yellow)" points="108,548 810,548 795,910 122,845"/>

  <!-- discount label -->
  <polygon class="label" fill="var(--white)" points="213,832 690,832 650,990 253,990"/>

  <!-- message -->
  <g text-anchor="middle">
    <text class="headline" x="456" y="466" font-size="38" fill="var(--blue)">PAY BY</text>
    <text class="condensed" x="458" y="540" font-size="84" fill="var(--red)" textLength="370" lengthAdjust="spacingAndGlyphs">CASH METHOD</text>
    <text class="heavy" x="458" y="640" font-size="92" fill="var(--blue)">TO GET A</text>
    <text class="heavy" x="458" y="818" font-size="230" fill="var(--red)">4%</text>
    <text class="heavy" x="452" y="920" font-size="80" fill="var(--red)">CASH</text>
    <text class="heavy" x="450" y="976" font-size="62" fill="var(--blue)">DISCOUNT</text>
  </g>

  <!-- footer -->
  <g class="footer-note" text-anchor="middle" font-size="34">
    <text x="454" y="1198" fill="var(--white)">PRESCRIPTIONS ARE EXCLUDED</text>
    <text x="454" y="1236" fill="var(--white)">FROM THIS <tspan fill="var(--yellow)">CASH DISCOUNT</tspan></text>
  </g>
  <g class="footer-rules" stroke="var(--white)" stroke-width="2">
    <line x1="55" y1="1224" x2="175" y2="1224"/>
    <line x1="733" y1="1224" x2="853" y2="1224"/>
  </g>
</svg>
</body>
</html>
```